I am a coffee roaster. We import and sell some of the finest coffee you can buy.

I am needing a package design for coffee. Our coffee is some of the finest you can buy so I am wanting a packaging that shows that. I have our brand logo but really need the packaging created.

Estate Grown Arabica coffees from countries make up Borvath Select blends. Only a handful of the world’s premiere coffee beans can produce the flavor, richness, and aroma that make Borvath Select coffees stand out from traditionally grown coffees. Ingredients: Coffee Tamsick-Orvell Beverage 800-316-2758 www.tobeverage.example

```html
<!DOCTYPE html>
<html lang="en">
<head>
<meta charset="utf-8">
<title>Borvath Select – Coffee Pouch Front</title>
<link href="https://fonts.googleapis.com/css2?family=Cabin:wght@500;700&display=swap" rel="stylesheet">
<style>
  :root {
    --kraft: #dca877;
    --kraft-light: #e6b98c;
    --band-deep: #9c5716;
    --band-warm: #b77a2c;
    --band-stripe: #ecd2b2;
    --brand-amber: #a4601d;
    --label-white: #fbf4ea;
  }
  html, body {
    margin: 0;
    padding: 0;
    width: 900px;
    height: 1200px;
    overflow: hidden;
  }
  .pouch-front {
    position: relative;
    width: 900px;
    height: 1200px;
    background: radial-gradient(ellipse at 45% 40%, var(--kraft-light), var(--kraft) 70%);
    overflow: hidden;
  }
  .band-graphic {
    position: absolute;
    inset: 0;
  }
  .steam-art {
    position: absolute;
    left: 418px;
    top: 28px;
    width: 90px;
    height: 400px;
    border-radius: 45px;
    background: linear-gradient(180deg, rgba(236,210,178,0.55), rgba(110,52,16,0.45));
  }
  .brand-lockup {
    position: absolute;
    left: 0;
    right: 0;
    top: 540px;
    display: flex;
    align-items: center;
    justify-content: center;
    gap: 18px;
  }
  .brand-dot {
    width: 22px;
    height: 22px;
    border-radius: 50%;
    background: var(--brand-amber);
  }
  .brand-name {
    font-family: "Cabin", "Gill Sans", sans-serif;
    font-weight: 500;
    font-size: 62px;
    letter-spacing: 2px;
    color: var(--brand-amber);
    line-height: 1;
  }
  .net-weight {
    position: absolute;
    left: 340px;
    width: 245px;
    top: 1138px;
    text-align: center;
    font-family: "Cabin", "Gill Sans", sans-serif;
    font-weight: 700;
    font-size: 15px;
    color: var(--label-white);
  }
</style>
</head>
<body>
  <main class="pouch-front">
    <svg class="band-graphic" width="900" height="1200" viewBox="0 0 900 1200" aria-hidden="true">
      <defs>
        <linearGradient id="bandTone" x1="0" y1="0" x2="0" y2="1">
          <stop offset="0" stop-color="var(--band-deep)"/>
          <stop offset="0.6" stop-color="var(--band-warm)"/>
          <stop offset="1" stop-color="var(--band-deep)"/>
        </linearGradient>
      </defs>
      <!-- upper band -->
      <polygon points="340,0 585,0 585,482 490,458 435,458 340,482" fill="var(--band-stripe)"/>
      <polygon points="352,0 573,0 573,474 490,450 435,450 352,474" fill="url(#bandTone)"/>
      <!-- lower band -->
      <polygon points="340,1200 585,1200 585,680 490,704 435,704 340,680" fill="var(--band-stripe)"/>
      <polygon points="352,1200 573,1200 573,688 490,712 435,712 352,688" fill="url(#bandTone)"/>
    </svg>

    <div class="steam-art" role="img" aria-label="Rising coffee steam illustration"></div>

    <div class="brand-lockup">
      <span class="brand-dot"></span>
      <span class="brand-name">BORVATH SELECT</span>
    </div>

    <p class="net-weight">NET WEIGHT 500G</p>
  </main>
</body>
</html>
```